We need a flyer design to promote Penhallow & Tibbs Landscaping and Lawn Maintenance.

The flyer needs to be have:-
1) A great head line ( When quality matters)
2) A really awesome offer ( no obligation free trial mow)
3) A sense of scarcity (Due to time restraints, we can only take limited number of free lawn jobs. This offer is only available to the first 20 callers)
4) A call to action (Call now to avoid disappointment)
5) Contact details (Penhallow & Tibbs Landscaping and Lawn Maintenance 0452 786 305)

The layout of the entire flyer should come across to potential customers as

1) simple to understand what Penhallow & Tibbs offer (not overcrowd with messages; the main aim is to communicate across our services.)

The list of services that Penhallow & Tibbs provide will be:-

- Lawn Mowing - Pruning - Weeding
- Mulching - Edging - Hedging
- Trimming - Fertilising - Garden maintenance
- Weekly, fortnightly or monthly programs

Thank you.

```html
<!DOCTYPE html>
<html lang="en">
<head>
<meta charset="utf-8">
<title>Penhallow &amp; Tibbs Landscaping – Flyer</title>
<link rel="stylesheet" href="https://fonts.googleapis.com/css2?family=Cinzel:wght@500;600;700&family=Mulish:wght@700;800&display=swap">
<style>
  :root {
    --backdrop: #e8e5df;
    --grass-light: #7cc644;
    --grass-mid: #4fa42c;
    --grass-dark: #2f7a1c;
    --brand-green: #45ad38;
    --brown: #3a2816;
    --cream: #fdf6c0;
    --yellow: #f2ea1c;
    --white: #ffffff;
  }
  * { box-sizing: border-box; margin: 0; padding: 0; }
  html, body { width: 1200px; height: 1000px; overflow: hidden; }
  body { background: var(--backdrop); position: relative; font-family: "Mulish", sans-serif; }

  .flyer {
    position: absolute; left: 287px; top: 58px;
    width: 625px; height: 884px; overflow: hidden;
    background: var(--white);
    box-shadow: 0 6px 24px rgba(0,0,0,.25);
  }
  .hero-photo {
    position: absolute; left: 0; top: 0; width: 625px; height: 560px;
    background:
      radial-gradient(ellipse at 78% 45%, rgba(40,40,40,.35) 0 14%, transparent 30%),
      linear-gradient(180deg, var(--grass-light), var(--grass-mid) 60%, var(--grass-dark));
  }
  .shapes { position: absolute; left: 0; top: 0; }

  .headline {
    position: absolute; left: 0; width: 406px; top: 52px;
    text-align: center; font-family: "Cinzel", serif; font-weight: 600;
    color: var(--white); line-height: .9; text-shadow: 0 2px 4px rgba(0,0,0,.35);
  }
  .headline span { display: block; }
  .headline .when { font-size: 66px; }
  .headline .quality { font-size: 63px; color: var(--yellow); }
  .headline .matters { font-size: 66px; }

  .scarcity-text {
    position: absolute; left: 90px; top: 290px; width: 156px;
    text-align: center; color: var(--cream);
    font-size: 16.5px; font-weight: 700; line-height: 21px;
  }
  .offer-text {
    position: absolute; left: 300px; top: 392px; width: 160px;
    text-align: center; color: var(--brown);
    font-size: 21px; font-weight: 800; line-height: 1.2;
  }
  .cta-text {
    position: absolute; left: 480px; top: 474px; width: 126px;
    text-align: center; color: var(--brown); font-weight: 800; line-height: 1.2;
  }
  .cta-text .big { display: block; font-size: 17px; }
  .cta-text .small { display: block; font-size: 11.5px; }

  .services { position: absolute; left: 38px; top: 536px; }
  .services h2 {
    font-family: "Cinzel", serif; font-weight: 600; font-size: 34px; line-height: 40px;
    color: var(--brown); letter-spacing: .3px; margin-bottom: 0;
  }
  .services ul { list-style: none; }
  .services li {
    color: var(--brand-green); font-size: 25.5px; font-weight: 800; line-height: 34px;
  }
  .divider {
    position: absolute; left: 38px; top: 728px; width: 566px;
    border-top: 2px dotted #9a9a9a;
  }

  .contact { position: absolute; left: 38px; top: 748px; display: flex; align-items: center; }
  .business-name {
    font-family: "Mulish", sans-serif; font-weight: 800; color: var(--brown);
    font-size: 16px; line-height: 1.3; width: 282px;
  }
  .business-name span { display: block; }
  .contact .rule { width: 2px; height: 56px; background: #8a8a8a; margin: 0 12px 0 6px; }
  .phone { display: flex; align-items: center; gap: 6px; color: var(--brown); font-weight: 800; font-size: 35px; }
</style>
</head>
<body>
  <main class="flyer">
    <div class="hero-photo" role="img" aria-label="Photo of a red lawn mower standing on freshly cut green grass"></div>

    <svg class="shapes" width="625" height="884" viewBox="0 0 625 884" aria-hidden="true">
      <path d="M0 492 C170 440 420 470 625 415 L625 884 L0 884 Z" fill="var(--brand-green)"/>
      <path d="M0 502 C180 455 420 485 625 428 L625 884 L0 884 Z" fill="var(--white)"/>
      <path d="M0 812 C200 860 450 840 625 780 L625 884 L0 884 Z" fill="var(--brand-green)"/>
      <path d="M0 822 C200 866 450 852 625 795 L625 810 C450 864 200 870 0 834 Z" fill="#8fd16a"/>

      <circle cx="170" cy="369" r="125" fill="var(--white)"/>
      <circle cx="170" cy="369" r="117" fill="var(--brown)"/>
      <g stroke="var(--white)" stroke-width="2.5">
        <line x1="170" y1="254" x2="170" y2="272"/><line x1="170" y1="466" x2="170" y2="484"/>
        <line x1="55" y1="369" x2="73" y2="369"/><line x1="267" y1="369" x2="285" y2="369"/>
        <line x1="227.5" y1="269.4" x2="222" y2="279"/><line x1="269.6" y1="311.5" x2="260" y2="317"/>
        <line x1="269.6" y1="426.5" x2="260" y2="421"/><line x1="227.5" y1="468.6" x2="222" y2="459"/>
        <line x1="112.5" y1="468.6" x2="118" y2="459"/><line x1="70.4" y1="426.5" x2="80" y2="421"/>
        <line x1="70.4" y1="311.5" x2="80" y2="317"/><line x1="112.5" y1="269.4" x2="118" y2="279"/>
      </g>

      <circle cx="380" cy="444" r="89" fill="var(--brown)"/>
      <circle cx="380" cy="444" r="82" fill="var(--cream)"/>

      <circle cx="543" cy="502" r="66" fill="var(--brand-green)"/>
      <circle cx="543" cy="502" r="63" fill="var(--white)"/>
    </svg>

    <h1 class="headline">
      <span class="when">WHEN</span>
      <span class="quality">QUALITY</span>
      <span class="matters">MATTERS</span>
    </h1>

    <p class="scarcity-text">Due to time restraints, we can only take limited number of free lawn jobs. This offer is only available to the first 20 callers</p>
    <p class="offer-text">NO OBLIGATION FREE TRIAL NOW</p>
    <p class="cta-text"><span class="big">CALL NOW</span><span class="small">TO AVOID DISAPPOINTMENT</span></p>

    <section class="services">
      <h2>OUR SERVICES</h2>
      <ul>
        <li>Lawn Mowing • Pruning • Weeding</li>
        <li>Mulching • Edging • Hedging • Trimming</li>
        <li>Fertilising • Garden maintenance</li>
        <li>Weekly, fortnightly or monthly programs</li>
      </ul>
    </section>

    <div class="divider"></div>

    <footer class="contact">
      <p class="business-name">
        <span>Penhallow &amp; Tibbs</span>
        <span>Landscaping and Lawn Maintenance</span>
      </p>
      <div class="rule"></div>
      <div class="phone">
        <svg width="16" height="34" viewBox="0 0 16 34" aria-hidden="true">
          <path d="M12 2 C5 3 2 10 2 17 C2 24 5 31 12 32 L14 25 L9 23 C8 19 8 15 9 11 L14 9 Z" fill="var(--brand-green)"/>
        </svg>
        <span>0452 786 305</span>
      </div>
    </footer>
  </main>
</body>
</html>
```